依頼詳細
クリニックのHPです。
https://kitase-naika.jp
チラシはA4サイズです。
自分のイメージとして、こんなチラシが好き、こんなのは嫌という例を添付しますので参考にしてください。
添付した資料は全部使う必要はありません(特に、外観、内観予想図)。
ソノワで印刷しますので、ソノワが対応しているデータ形式でお願いします(ソノワにデータ作成テンプレートがあります)。
https://sonowa.com/guide/how-to-make-data/pamphlet/
クリニックがまだできていないので、外観予想図、内観予想図を添付します。
クリニック用のリーフレットデザインも別コンペで募集しています。
記載項目
開催日 2020年5月10日土曜日、場所、地図、アクセス
サイズ
A4
ページ数
片面
希望イメージ
シンプル 複雑
単色 カラフル
暗い 明るい
日常 高級
遊び心 厳粛
未来的 伝統的
女性的 男性的
希望する色
黄・オレンジ系、緑系、水色系
■ 選んだ理由

全体にバランスが良く、第一印象が良かったです。

■ 提案者全員のお礼・コメント

多くの皆様に応募していただき、ありがとうございます
良いデザイン案が多く、選ぶのに苦慮しました。今後も、仕事を依頼することがあると思いますが、よろしくお願いします。

```html
<!DOCTYPE html>
<html lang="ja">
<head>
<meta charset="utf-8">
<title>北瀬みなと内科 内覧会</title>
<link rel="stylesheet" href="https://fonts.googleapis.com/css2?family=Noto+Sans+JP:wght@400;500;700;900&family=Montserrat:wght@600;700&display=swap">
<style>
  :root {
    --blue: #2f7fd2;
    --blue-deep: #1f66b5;
    --blue-pale: #dcebf8;
    --grey-pale: #eceff2;
    --green: #4bb37c;
    --ink: #2b2b2b;
    --white: #ffffff;
  }
  * { margin: 0; padding: 0; box-sizing: border-box; }
  html, body { width: 854px; height: 1200px; overflow: hidden; background: var(--white); }
  .flyer {
    position: relative; width: 854px; height: 1200px; overflow: hidden;
    font-family: "Noto Sans JP", sans-serif; color: var(--ink); background: var(--white);
  }
  .backdrop { position: absolute; inset: 0; }
  .event-date {
    position: absolute; left: 34px; top: 18px;
    font-family: "Montserrat", sans-serif; font-weight: 700; font-size: 84px;
    color: var(--blue); letter-spacing: 1px; white-space: nowrap;
  }
  .event-date .weekday { font-family: "Noto Sans JP", sans-serif; font-size: 40px; font-weight: 700; vertical-align: 28px; }
  .event-time {
    position: absolute; left: 40px; top: 122px;
    font-family: "Montserrat", sans-serif; font-weight: 600; font-size: 26px; color: var(--blue);
    letter-spacing: 2px; white-space: nowrap;
  }
  .access-map {
    position: absolute; left: 420px; top: 28px; width: 400px; height: 210px;
    background: linear-gradient(135deg, #f4f7fa, #e3eaf1);
    border: 1px solid #cfd8e2;
  }
  .title-banner {
    position: absolute; left: 0; top: 262px; width: 430px; height: 136px;
    background: var(--blue); border: 6px solid var(--white); border-left: none;
    outline: 4px solid var(--blue);
    display: flex; align-items: center; justify-content: center;
  }
  .title-banner h1 {
    color: var(--white); font-weight: 900; font-size: 100px; letter-spacing: 6px; line-height: 1;
  }
  .opening {
    position: absolute; left: 430px; top: 420px; width: 400px;
    font-size: 28px; font-weight: 500; text-align: center; white-space: nowrap;
    padding-bottom: 8px; border-bottom: 2px solid var(--ink);
  }
  .brand-mark {
    position: absolute; left: 60px; top: 470px; width: 190px; height: 190px;
    border-radius: 50%; background: var(--blue-pale);
  }
  .clinic-name {
    position: absolute; left: 478px; top: 568px;
    display: flex; align-items: center; gap: 14px; white-space: nowrap;
  }
  .clinic-name .dot { width: 30px; height: 30px; border-radius: 50%; background: var(--blue); }
  .clinic-name .jp { font-size: 40px; font-weight: 500; letter-spacing: 2px; }
  .clinic-name-en {
    position: absolute; left: 522px; top: 632px; font-size: 18px; letter-spacing: 1px; white-space: nowrap;
  }
  .services { position: absolute; left: 470px; top: 676px; display: flex; gap: 14px; }
  .services li {
    list-style: none; width: 104px; height: 36px; border-radius: 18px;
    background: var(--green); color: var(--white); font-size: 18px; font-weight: 500;
    display: flex; align-items: center; justify-content: center;
  }
  .message { position: absolute; left: 40px; top: 752px; width: 780px; }
  .message h2 { font-size: 24px; font-weight: 700; margin-bottom: 14px; white-space: nowrap; }
  .message p { font-size: 18.5px; line-height: 1.68; text-align: justify; }
  .scenery {
    position: absolute; left: 0; bottom: 0; width: 854px; height: 230px;
    background: linear-gradient(180deg, rgba(255,255,255,0) 0%, #e8f1ea 55%, #c9dfcb 100%);
  }
  .contact {
    position: absolute; left: 44px; top: 1062px;
    display: flex; align-items: center; gap: 14px; white-space: nowrap;
    font-family: "Montserrat", sans-serif; font-weight: 600; font-size: 34px; letter-spacing: 2px;
  }
  .director { position: absolute; right: 44px; top: 1096px; font-size: 18px; white-space: nowrap; }
</style>
</head>
<body>
<div class="flyer">
  <svg class="backdrop" width="854" height="1200" viewBox="0 0 854 1200" aria-hidden="true">
    <polygon points="0,0 300,0 0,260" fill="var(--blue-pale)"/>
    <polygon points="854,240 854,760 560,520" fill="var(--grey-pale)"/>
    <polygon points="0,420 220,560 0,700" fill="var(--blue-pale)" opacity="0.6"/>
  </svg>

  <div class="event-date">5.10<span class="weekday">(日)</span></div>
  <div class="event-time">00:00 ～ 00:00</div>

  <div class="access-map" role="img" aria-label="クリニック周辺のアクセス地図"></div>

  <div class="title-banner"><h1>内覧会</h1></div>

  <div class="opening">2020年 5月〇日（〇）開院</div>

  <div class="brand-mark" aria-hidden="true"></div>

  <div class="clinic-name"><span class="dot"></span><span class="jp">北瀬みなと内科</span></div>
  <div class="clinic-name-en">Kitase Minato Clinic</div>

  <ul class="services">
    <li>一般内科</li><li>一般内科</li><li>一般内科</li>
  </ul>

  <div class="scenery" role="img" aria-label="芝生と新しいクリニック外観のイメージ写真"></div>

  <section class="message">
    <h2>地域の皆さまによりそう総合内科の「かかりつけ医」をめざして</h2>
    <p>プライマリ・ケア（Primary care）とは、患者さんが抱える心身の問題を幅広く診察するトレーニングを受けた医師がおこなう医療です。高血圧や糖尿病などの生活習慣病の治療が必要な方、頭痛やめまいで困っている方、物忘れや認知症が心配な方、原因がわからない体調不良が心配な方、予防接種を受けたい方、治療が必要だけど通院できない方など、さまざまな患者さんのニーズにきちんと向き合い、患者さん一人ひとりに寄りそう医療を提供し、気軽に相談していただけるクリニックづくりをめざしています。今後ともよろしくお願い申し上げます。</p>
  </section>

  <div class="contact">
    <svg width="30" height="30" viewBox="0 0 24 24" aria-hidden="true"><path fill="var(--ink)" d="M6.6 10.8a15.1 15.1 0 0 0 6.6 6.6l2.2-2.2a1 1 0 0 1 1-.25 11.4 11.4 0 0 0 3.6.6 1 1 0 0 1 1 1V20a1 1 0 0 1-1 1A17 17 0 0 1 3 4a1 1 0 0 1 1-1h3.5a1 1 0 0 1 1 1c0 1.25.2 2.45.6 3.6a1 1 0 0 1-.25 1z"/></svg>
    <span>03-5555-0123</span>
  </div>
  <div class="director">院長　港田健司</div>
</div>
</body>
</html>
```